"Parker's True Grain Woodwork" with a logo of a saw blade and handplane combined

Need a business card logo with a saw blade and hand plane
combined with Parker's True Grain Woodwork on it, and a unique design.

Woodworking has been in my family for generations, from carpentry, to milling logs for old farm homes and barns in the 1930's and 1940's. My grandfather had a small carpentry business from his home,and passed his skills down to my father who also did woodworking from his own small business. Having the passion for woodwork in my blood, I'm trying to continue with my own small business doing custom fine woodwork such as tables, small cabinetry and even outdoor projects to suite the customers needs. All my projects start with a rough piece of lumber, what ever the species suited for the project, and is milled to dimensions , assembled, and finished all by hand for a true handcrafted project.

My target market would be people who want a custom handmade piece, something that they can't find in stores and is unique. Also people who are willing to pay and appreciate the value, which is sometimes a hard market to find.

As far as design, I think I would like to get a sleek looking saw blade on the card combined with a hand plane some how. Background colour maybe a dark wood texture or grey? Colours I like are grey, black, reds, white, yellows but depending on how the card is looking I'm not afraid to use a cool colour to make something stand out. Just want the card to flow ,look clean and unique. Lettering I like serif and script or something similar to these that looks good on the card.

Facebook page is under Parker's True Grain Woodwork
Updates

If I could get logo on the card, a saw blade, hand plane or combine both together would be nice! Added Saturday, June 11, 2016

Target Market(s)

People that like a unique hand made project built to last

Industry/Entity Type

Business

Contact Information for Business Card

Parkers True Grain Woodwork
Hand crafted by: Owen Parker
Phone: 555 618-2297
Address: 412 Birchview Rd. Fernwick-By-The-Creek Prov.
Email: parkerstruegrain@mailbox-example.com
Facebook: Parkers True Grain Woodwork
prefer icons for the info!

Font styles to use
Serif
Script

Requirements
Must have
• Nice clean look, little bit bold with an elegant taste
• Prefer black lettering
Nice to have
• I like silver for the saw blade and silver with brown handles on the hand plane!
Should not have
• Bright colours

```html
<!DOCTYPE html>
<html lang="en">
<head>
<meta charset="utf-8">
<title>Parkers True Grain Woodwork – Business Card</title>
<link rel="stylesheet" href="https://fonts.googleapis.com/css2?family=Roboto:wght@400;500;700&display=swap">
<style>
  :root {
    --stage: #1b1b1b;
    --card-dark: #0e0e0e;
    --card-mid: #262626;
    --silver: #cfcfcf;
    --silver-deep: #9a9a9a;
    --text-light: #f2f2f2;
    --text-soft: #d2d2d2;
    --accent: #c8692a;
  }
  * { margin: 0; padding: 0; box-sizing: border-box; }
  html, body {
    width: 1200px; height: 800px; overflow: hidden;
    background: var(--stage);
    font-family: "Roboto", Arial, sans-serif;
  }
  .canvas {
    width: 1200px; height: 800px;
    display: flex; align-items: center; justify-content: center;
  }
  .business-card {
    position: relative;
    width: 1000px; height: 570px;
    overflow: hidden;
    box-shadow: 0 18px 40px rgba(0,0,0,.6);
  }
  .card-backdrop {
    position: absolute; inset: 0;
    background: radial-gradient(ellipse at 55% 40%, var(--card-mid) 0%, var(--card-dark) 75%);
  }
  .card-content {
    position: relative;
    height: 100%;
    display: flex; flex-direction: column; align-items: center;
    padding: 44px 60px;
  }
  .brand-mark {
    width: 170px; height: 170px; border-radius: 50%;
    background: linear-gradient(160deg, var(--silver) 0%, var(--silver-deep) 100%);
  }
  .brand-name {
    margin-top: 22px;
    font-size: 44px; font-weight: 700; letter-spacing: 2px;
    text-transform: uppercase;
    color: var(--silver);
    white-space: nowrap;
  }
  .contact-block {
    margin-top: 30px;
    display: flex; flex-direction: column; align-items: flex-start;
  }
  .maker-line {
    font-size: 24px; font-weight: 500; letter-spacing: .5px;
    color: var(--text-light); text-transform: uppercase;
    margin-bottom: 10px;
  }
  .contact-line {
    display: flex; align-items: center; gap: 12px;
    font-size: 21px; color: var(--text-soft);
    line-height: 30px;
    white-space: nowrap;
  }
  .contact-icon { width: 20px; height: 20px; flex: none; }
  .social-square { width: 18px; height: 18px; background: var(--accent); flex: none; margin: 0 1px; }
</style>
</head>
<body>
<main class="canvas">
  <article class="business-card">
    <div class="card-backdrop" role="img" aria-label="Dark charcoal wood grain background"></div>
    <div class="card-content">
      <div class="brand-mark" aria-hidden="true"></div>
      <h1 class="brand-name">Parkers True Grain Woodwork</h1>
      <div class="contact-block">
        <p class="maker-line">Hand crafted by: Owen Parker</p>
        <p class="contact-line">
          <svg class="contact-icon" viewBox="0 0 20 20" aria-hidden="true"><path d="M10 1a6 6 0 0 0-6 6c0 4.5 6 12 6 12s6-7.5 6-12a6 6 0 0 0-6-6zm0 8.5A2.5 2.5 0 1 1 10 4.5a2.5 2.5 0 0 1 0 5z" fill="var(--accent)"/></svg>
          412 Birchview Rd. Fernwick-By-The-Creek Prov.
        </p>
        <p class="contact-line">
          <svg class="contact-icon" viewBox="0 0 20 20" aria-hidden="true"><path d="M5 2h3l1.5 4-2 1.3a10 10 0 0 0 5.2 5.2l1.3-2 4 1.5v3a2 2 0 0 1-2 2A15 15 0 0 1 3 4a2 2 0 0 1 2-2z" fill="var(--accent)"/></svg>
          555 618-2297
        </p>
        <p class="contact-line">
          <svg class="contact-icon" viewBox="0 0 20 20" aria-hidden="true"><rect x="1.5" y="4" width="17" height="12" rx="1.5" fill="var(--accent)"/><path d="M2 5l8 6 8-6" fill="none" stroke="var(--card-dark)" stroke-width="1.5"/></svg>
          parkerstruegrain@mailbox-example.com
        </p>
        <p class="contact-line">
          <span class="social-square" aria-hidden="true"></span>
          Parker's True Grain Woodwork
        </p>
      </div>
    </div>
  </article>
</main>
</body>
</html>
```